Dravel

We are openıng one huntıng showroom in Riyadh? Saudi Arabia. Company name is "DRAVEL".
Our logo designed and we need Business Card Design now.
I attached DRAVEL logo below.
Front side will English and back side will be Arabic

```html
<!DOCTYPE html>
<html lang="en">
<head>
<meta charset="utf-8">
<title>Dravel Business Card</title>
<link href="https://fonts.googleapis.com/css2?family=Lato:wght@400;700;900&family=Varela+Round&display=swap" rel="stylesheet">
<style>
  :root {
    --green-dark: #08794a;
    --green-light: #78a03a;
    --paper: #ffffff;
    --backdrop: #3a3a3a;
  }
  html, body {
    margin: 0;
    width: 1200px;
    height: 900px;
    overflow: hidden;
    background: var(--backdrop);
  }
  .card {
    position: absolute;
    left: 100px;
    top: 160px;
    width: 1000px;
    height: 580px;
    background: var(--paper);
    border-radius: 34px;
    overflow: hidden;
    font-family: "Lato", sans-serif;
  }
  .card-waves {
    position: absolute;
    inset: 0;
    width: 1000px;
    height: 580px;
  }
  .brand-name {
    position: absolute;
    left: 64px;
    top: 38px;
    margin: 0;
    font-family: "Lato", sans-serif;
    font-weight: 900;
    font-size: 96px;
    letter-spacing: 2px;
    color: var(--green-dark);
    line-height: 1;
  }
  .location {
    position: absolute;
    left: 92px;
    top: 172px;
    margin: 0;
    font-family: "Varela Round", sans-serif;
    font-weight: 400;
    font-size: 24px;
    color: var(--green-dark);
    font-weight: bold;
  }
  .person {
    position: absolute;
    right: 80px;
    top: 196px;
    text-align: right;
    font-family: "Varela Round", sans-serif;
  }
  .person-name {
    margin: 0;
    font-size: 40px;
    font-weight: bold;
    color: var(--green-dark);
    line-height: 1.1;
  }
  .person-title {
    margin: 0;
    font-size: 25px;
    font-weight: bold;
    color: var(--green-light);
  }
  .contacts {
    position: absolute;
    right: 56px;
    top: 398px;
    margin: 0;
    padding: 0;
    list-style: none;
  }
  .contact {
    display: flex;
    justify-content: flex-end;
    align-items: center;
    gap: 14px;
    height: 40px;
    margin-bottom: 4px;
    color: var(--paper);
    font-size: 30px;
    font-weight: 400;
  }
  .contact-icon {
    width: 34px;
    height: 34px;
    background: var(--green-light);
    display: flex;
    align-items: center;
    justify-content: center;
  }
  .contact-icon svg {
    width: 22px;
    height: 22px;
  }
</style>
</head>
<body>
  <section class="card" aria-label="Dravel business card">
    <svg class="card-waves" viewBox="0 0 1000 580" aria-hidden="true">
      <path d="M0,200 C90,270 220,320 470,338 C240,338 80,300 0,238 Z" fill="var(--green-light)"/>
      <path d="M0,258 C150,350 320,372 540,372 C740,372 900,330 1000,236 L1000,580 L0,580 Z" fill="var(--green-dark)"/>
      <path d="M60,292 C220,362 520,368 860,380 C520,378 220,380 60,302 Z" fill="var(--paper)"/>
    </svg>

    <h1 class="brand-name">DRAVEL</h1>
    <p class="location">Riyadh, Saudi Arabia</p>

    <div class="person">
      <p class="person-name">Your Name</p>
      <p class="person-title">Managing Director</p>
    </div>

    <ul class="contacts">
      <li class="contact">
        <span>214-555-0187</span>
        <span class="contact-icon">
          <svg viewBox="0 0 24 24"><path d="M6.6 10.8a15 15 0 0 0 6.6 6.6l2.2-2.2a1 1 0 0 1 1-.25 11 11 0 0 0 3.6.6 1 1 0 0 1 1 1V20a1 1 0 0 1-1 1A17 17 0 0 1 3 4a1 1 0 0 1 1-1h3.5a1 1 0 0 1 1 1 11 11 0 0 0 .6 3.6 1 1 0 0 1-.25 1z" fill="#fff"/></svg>
        </span>
      </li>
      <li class="contact">
        <span>info@dravel.com</span>
        <span class="contact-icon">
          <svg viewBox="0 0 24 24"><rect x="3" y="6" width="18" height="12" fill="none" stroke="#fff" stroke-width="2"/><path d="M3 6l9 7 9-7M3 18l7-6M21 18l-7-6" fill="none" stroke="#fff" stroke-width="1.6"/></svg>
        </span>
      </li>
      <li class="contact">
        <span>www.yourwebsitehere.com</span>
        <span class="contact-icon">
          <svg viewBox="0 0 24 24"><g fill="none" stroke="#fff" stroke-width="1.6"><circle cx="12" cy="12" r="9"/><ellipse cx="12" cy="12" rx="4" ry="9"/><path d="M3 12h18M5 7h14M5 17h14"/></g></svg>
        </span>
      </li>
    </ul>
  </section>
</body>
</html>
```